Wills & Estates legal firm needing A4 presentation folder design

We need a more corporate but family orientated looking presentation folder incorporating existing logo. Needs to be clean lines but warm not clinical. Will contain all documents a family needs when someone dies. Not looking for traditional legal symbols of scales etc. Potential that the design can flow through to letterhead, document front covers, brochures, business cards etc for a complete corporate identity. We are only a firm of one fee earner and cater to a mum and dad market

Industry/Entity Type

Law Firm

Font styles to use
Other font styles liked:
• Univers LT std 57 cn

Colors
ec1f27
848484

Requirements
Must have
• Existing logo
• Area for contact details on back of folder
• Incorporating existing red an grey colours
Should not have
• legal symbols

```html
<!DOCTYPE html>
<html lang="en">
<head>
<meta charset="utf-8">
<title>Hearthline Legal – Presentation Folder</title>
<link href="https://fonts.googleapis.com/css2?family=Roboto+Condensed:wght@400;500&display=swap" rel="stylesheet">
<style>
  :root {
    --stage: #000000;
    --brand-red: #c41230;
    --brand-red-deep: #8a0d1f;
    --brand-grey: #848484;
    --paper: #ffffff;
    --ink: #2f3a44;
  }
  html, body {
    margin: 0;
    padding: 0;
    width: 1200px;
    height: 900px;
    overflow: hidden;
    background: var(--stage);
  }
  .stage {
    position: relative;
    width: 1200px;
    height: 900px;
  }
  .folder-panel {
    position: absolute;
    left: 290px;
    width: 620px;
    height: 402px;
    display: block;
  }
  .folder-outside { top: 28px; }
  .folder-inside { top: 470px; }
  .brand-name {
    font-family: "Roboto Condensed", Arial Narrow, sans-serif;
    font-weight: 400;
    fill: var(--brand-red);
  }
  .contact-block {
    font-family: "Roboto Condensed", Arial Narrow, sans-serif;
    font-size: 5px;
    fill: var(--paper);
  }
  .card-label {
    font-family: "Roboto Condensed", Arial Narrow, sans-serif;
    font-weight: 500;
    font-size: 14px;
    fill: #222;
  }
  .pocket-quote {
    font-family: "Roboto Condensed", Arial Narrow, sans-serif;
    font-size: 14px;
    fill: var(--paper);
  }
</style>
</head>
<body>
<main class="stage">

  <!-- Outside spread: back cover (left) and front cover (right) -->
  <svg class="folder-panel folder-outside" viewBox="0 0 673 437" aria-label="Folder outside spread">
    <defs>
      <linearGradient id="outsideShade" x1="0.35" y1="0" x2="1" y2="1">
        <stop offset="0" stop-color="var(--brand-red)"/>
        <stop offset="0.45" stop-color="var(--brand-red-deep)"/>
        <stop offset="0.75" stop-color="#a4102a"/>
        <stop offset="1" stop-color="var(--brand-red)"/>
      </linearGradient>
      <linearGradient id="sweepShade" x1="0" y1="0" x2="1" y2="0.6">
        <stop offset="0" stop-color="#9c0f25"/>
        <stop offset="0.5" stop-color="var(--brand-red)"/>
        <stop offset="1" stop-color="var(--brand-red)"/>
      </linearGradient>
      <linearGradient id="innerSweep" x1="0" y1="0" x2="1" y2="1">
        <stop offset="0" stop-color="#b01229"/>
        <stop offset="1" stop-color="var(--brand-red)"/>
      </linearGradient>
    </defs>
    <rect class="panel-base" width="673" height="437" fill="var(--brand-red)"/>
    <rect class="panel-shade" width="673" height="437" fill="url(#outsideShade)" opacity="0.85"/>
    <path class="cover-sweep" d="M338 0 Q400 240 673 258 L673 0 Z" fill="url(#sweepShade)"/>
    <path class="cover-sweep-inner" d="M468 0 Q500 200 673 236 L673 0 Z" fill="url(#innerSweep)"/>
    <path class="logo-tab" d="M452 313 H673 V373 H452 Q439 373 439 360 V326 Q439 313 452 313 Z" fill="var(--paper)"/>
    <text class="brand-name" x="556" y="354" font-size="27" text-anchor="middle">Hearthline Legal</text>
    <g class="contact-block" text-anchor="middle">
      <text x="170" y="400">412 LINDEN ROW E</text>
      <text x="170" y="407">HARBOR CITY WA 98230</text>
      <text x="170" y="414">USA</text>
    </g>
  </svg>

  <!-- Inside spread with pocket -->
  <svg class="folder-panel folder-inside" viewBox="0 0 673 437" aria-label="Folder inside spread">
    <defs>
      <linearGradient id="pocketShade" x1="0" y1="0" x2="1" y2="1">
        <stop offset="0" stop-color="#9a0e24"/>
        <stop offset="0.6" stop-color="var(--brand-red)"/>
        <stop offset="1" stop-color="var(--brand-red)"/>
      </linearGradient>
    </defs>
    <rect class="panel-base" width="673" height="437" fill="var(--paper)"/>
    <text class="brand-name" x="35" y="233" font-size="40">Hearthline Legal</text>
    <path class="pocket" d="M347 437 Q350 230 560 225 Q630 228 673 258 L673 437 Z" fill="var(--brand-red)"/>
    <path class="pocket-fold" d="M360 437 Q380 300 560 290 Q630 292 673 310 L673 437 Z" fill="url(#pocketShade)"/>
    <path class="pocket-fold-top" d="M400 330 Q470 290 560 290 Q630 292 673 310 L673 300 Q620 270 560 272 Q460 280 400 330 Z" fill="var(--brand-red)" opacity="0.9"/>
    <path class="card-slot" d="M476 277 H595 V338 L581 352 H462 V291 Z" fill="var(--paper)"/>
    <text class="card-label" x="528" y="320" text-anchor="middle">Calling Card</text>
    <g class="pocket-quote" text-anchor="middle">
      <text x="518" y="384">“Neque porro quisquam est qui</text>
      <text x="518" y="403">dolorem ipsum quia dolor sit amet”</text>
    </g>
  </svg>

</main>
</body>
</html>
```